Letterhead, stationery and email signature for construction business

I need the letterhead, stationery and email signature designs for a construction business. I want them to have a corporate feel to them.

I've attached the logo for reference.

```html
<!DOCTYPE html>
<html lang="en">
<head>
<meta charset="utf-8">
<title>Brickmont Projects – Email Signature</title>
<link href="https://fonts.googleapis.com/css2?family=Montserrat:ital,wght@0,400;0,500;0,700;1,300&display=swap" rel="stylesheet">
<style>
  :root {
    --brand-blue: #3057a0;
    --text-blue: #2f55a4;
    --band-grey: #52525e;
    --paper: #ffffff;
  }
  * { margin: 0; padding: 0; box-sizing: border-box; }
  html, body { width: 1200px; height: 441px; overflow: hidden; background: var(--paper); }
  .signature {
    position: relative;
    width: 1200px;
    height: 441px;
    overflow: hidden;
    background: var(--paper);
    font-family: "Montserrat", Arial, sans-serif;
    color: var(--text-blue);
  }
  .signature__shapes { position: absolute; inset: 0; }
  .brand {
    position: absolute;
    left: 197px;
    top: 227px;
    display: flex;
    align-items: center;
    gap: 12px;
    color: var(--paper);
    font-weight: 700;
  }
  .brand__mark { width: 56px; height: 56px; background: var(--paper); }
  .brand__name { line-height: 1; }
  .brand__name-main { display: block; font-size: 35px; letter-spacing: -0.5px; }
  .brand__name-sub { display: block; font-size: 15px; letter-spacing: 9.4px; margin-top: 6px; }
  .person {
    position: absolute;
    right: 100px;
    top: 66px;
    text-align: right;
  }
  .person__name { font-size: 22px; font-weight: 500; line-height: 1.2; }
  .person__role { font-size: 21px; font-weight: 300; font-style: italic; line-height: 1.25; letter-spacing: 0.3px; }
  .contact {
    position: absolute;
    right: 100px;
    top: 154px;
    text-align: right;
    font-size: 15.5px;
    font-weight: 400;
    line-height: 18.8px;
  }
  .social {
    position: absolute;
    top: 257px;
    left: 976px;
    display: flex;
    gap: 25px;
  }
  .social__dot { width: 25px; height: 25px; border-radius: 50%; background: var(--paper); }
  .web {
    position: absolute;
    right: 93px;
    top: 331px;
    text-align: right;
    font-size: 15.5px;
    line-height: 19px;
  }
</style>
</head>
<body>
  <div class="signature">
    <svg class="signature__shapes" width="1200" height="441" viewBox="0 0 1200 441" aria-hidden="true">
      <rect class="band" x="500" y="248" width="700" height="46" fill="var(--band-grey)"/>
      <polygon class="panel" points="220,0 738,0 467,441 0,441 0,357" fill="var(--brand-blue)"/>
    </svg>

    <div class="brand">
      <span class="brand__mark"></span>
      <span class="brand__name">
        <span class="brand__name-main">BRICKMONT</span>
        <span class="brand__name-sub">PROJECTS</span>
      </span>
    </div>

    <div class="person">
      <p class="person__name">Laura Penning</p>
      <p class="person__role">Marketing Specialist</p>
    </div>

    <div class="contact">
      <p>Adress, City</p>
      <p>Area State Code</p>
      <p>+1 (555) 014-2290</p>
    </div>

    <div class="social" aria-label="Social links">
      <span class="social__dot"></span>
      <span class="social__dot"></span>
      <span class="social__dot"></span>
    </div>

    <div class="web">
      <p>info@brickmontprojects.com</p>
      <p>www.website.com</p>
    </div>
  </div>
</body>
</html>
```